Report-Design  für Social-Media-Beratungs-Agentur
Report-Design für Social-Media-Beratungs-Agentur
Zielgruppe
Wir sind eine Social-Media-Beratungs-Agentur, die KMU bei der strategischen Ausrichtung und Umsetzung ihrer Social-Media-Präsenzen berät und unterstützt.
Aufgabenstellung
Wir analysieren die KarriNetz Profile von Unternehmen in einer Excel-Datei, indem wir in einem Reiter verschiedene Aspekte bewerten. Aus diesen Bewertungen ergibt sich dann in einem zweiten Reiter ein Report (hängt hier an), in den die Ergebnisse aus der 1. Mappe automatisch übernommen werden. Dieser Report wird als PDF gespeichert und an den Kunden geschickt. Wir möchten das Report-Design gerne neu gestalten lassen: Es soll zeitgemäß, professionell und kompetent wirken und nicht mehr 'wie in Excel zusammengebastelt'. Ein Beispiel für ein Design, das uns gefällt, hängt als Inspiration an. Gerne können Grafikelemente aus Canva oder anderen Grafikprogrammen eingefügt werden. Wichtig ist, dass die Struktur mit den Zellen, in die Daten automatisch übernommen werden (im Anhang durch # gekennzeichnet), erhalten bleibt. Unsere Firmenfarben sind: #f69f25, #11323a, #809398, #fcfefd. Wir haben noch weitere Analysen, die wir bei Erfolg dieses Auftrags ebenfalls gerne optimieren lassen möchten.

```html
<!DOCTYPE html>
<html lang="de">
<head>
<meta charset="utf-8">
<title>Report – Social-Media-Analyse</title>
<link href="https://fonts.googleapis.com/css2?family=Montserrat:wght@400;500;600;700;800&display=swap" rel="stylesheet">
<style>
  :root{
    --orange:#f69f25;
    --petrol:#11323a;
    --slate:#809398;
    --paper:#fcfefd;
    --stage:#b3b3b3;
    --band:#ededed;
    --ink:#3c3c3c;
  }
  *{margin:0;padding:0;box-sizing:border-box}
  html,body{width:1200px;height:1117px;overflow:hidden}
  body{background:var(--stage);font-family:'Montserrat',sans-serif;position:relative}
  .report{position:absolute;left:250px;top:63px;width:700px;height:990px;background:#fff;box-shadow:6px 10px 18px rgba(0,0,0,.28);overflow:hidden}
  .hero{position:absolute;left:0;top:22px;width:700px;height:289px;
    background:
      linear-gradient(rgba(20,10,10,.25),rgba(20,10,10,.25)),
      linear-gradient(115deg,#8d9399 0%,#6c6f72 18%,#2b1c1c 30%,#4a3a35 55%,#7a6456 78%,#9c8170 100%)}
  .logo-tab{position:absolute;left:172px;top:22px;width:356px;height:82px}
  .brand{position:absolute;left:0;width:700px;text-align:center;color:var(--petrol)}
  .brand-name{top:24px;font-size:42px;font-weight:500;letter-spacing:1px;line-height:1}
  .brand-tag{top:71px;font-size:13px;font-weight:700;letter-spacing:.3px}
  .headline{position:absolute;left:0;top:124px;width:700px;text-align:center;color:#fff;font-weight:800;font-size:31px;line-height:32px}
  .subline{position:absolute;left:0;top:195px;width:700px;text-align:center;color:#fff;font-weight:700;font-size:15px;line-height:21px}
  .meta{position:absolute;left:149px;top:251px;height:29px;display:flex;font-size:14px;color:#fff;white-space:nowrap;filter:drop-shadow(0 2px 2px rgba(0,0,0,.35))}
  .meta-author{background:var(--petrol);border-radius:15px 0 0 15px;padding:0 28px 0 17px;line-height:29px;white-space:nowrap}
  .meta-date{background:var(--orange);border-radius:15px;padding:0 13px;line-height:29px;margin-left:-14px;white-space:nowrap}
  .meta b{font-weight:700}
  .goal{position:absolute;left:0;top:329px;width:284px;height:434px;background:var(--petrol);border-radius:0 8px 8px 0;color:#fff}
  .goal h2{position:absolute;left:65px;top:72px;font-size:19px;font-weight:800;color:var(--orange)}
  .goal p{position:absolute;left:65px;width:215px;font-size:12px;line-height:17.9px;white-space:nowrap}
  .goal .p1{top:109px}
  .goal .p2{top:216px}
  .goal-rule{position:absolute;left:135px;top:381px;width:55px;height:4px;background:var(--orange)}
  .criterion{position:absolute;left:304px;width:340px}
  .criterion svg{position:absolute;left:0;top:0;width:52px;height:60px}
  .criterion h3{position:absolute;left:65px;top:0;font-size:12px;font-weight:800;color:var(--orange);white-space:nowrap}
  .criterion p{position:absolute;left:65px;width:275px;font-size:11px;line-height:14.8px;color:var(--ink);white-space:nowrap}
  .divider{position:absolute;left:306px;width:327px;border-top:1px dashed var(--orange)}
  .recommend-band{position:absolute;left:0;top:804px;width:700px;height:118px;background:var(--band)}
  .banner-ring{position:absolute;left:32px;top:786px;width:636px;height:40px;border-radius:20px;border:4px solid #fff;border-top-color:transparent;background:transparent}
  .banner{position:absolute;left:40px;top:789px;width:619px;height:29px;border-radius:15px;background:var(--orange);color:#fff;font-weight:800;font-size:16px;line-height:30px;text-align:center}
  .tip{position:absolute;top:834px;width:180px}
  .tip svg{position:absolute;left:-21px;top:1px;width:11px;height:11px}
  .tip p{font-size:11.5px;line-height:14.6px;font-weight:700;color:#555;white-space:nowrap}
  .note{position:absolute;left:0;top:891px;width:700px;text-align:center;font-size:7px;line-height:10px;color:#666}
  .footer{position:absolute;left:0;top:922px;width:700px;height:68px;background:var(--petrol);color:#fff;font-size:11.5px}
  .footer .sep{position:absolute;top:15px;width:1px;height:30px;background:var(--orange)}
  .footer .item{position:absolute;text-align:center;white-space:nowrap}
  .footer svg{width:12px;height:12px}
</style>
</head>
<body>
<main class="report">
  <div class="hero" role="img" aria-label="Foto: Hand tippt auf einer Laptop-Tastatur, daneben ein Smartphone"></div>
  <svg class="logo-tab" viewBox="0 0 356 82" aria-hidden="true"><path d="M0 0 C28 0 38 10 53 40 C68 72 80 82 108 82 H248 C276 82 288 72 303 40 C318 10 328 0 356 0 Z" fill="#fff"/></svg>
  <div class="brand brand-name">KALTRIO</div>
  <div class="brand brand-tag">social media beratung</div>

  <h1 class="headline">OPTIMIEREN SIE IHRE<br>SOCIAL-MEDIA-NUTZUNG</h1>
  <p class="subline">STRATEGISCHER ANSATZ. ZEITSPARENDE<br>REDAKTION MIT KI. ECHTE ERGEBNISSE.</p>
  <div class="meta">
    <span class="meta-author">Erstellt durch: <b>Carla Westrup</b></span>
    <span class="meta-date">Datum: <b>23.07.2025</b></span>
  </div>

  <section class="goal">
    <h2>ZIEL DER ANALYSE</h2>
    <p class="p1">Diese Analyse zeigt, wie gut<br>Ihr KarriNetz-Unternehmensprofil<br>die Potenziale von Social Media<br>bereits nutzt - und wo noch<br>ungenutzte Chancen liegen.</p>
    <p class="p2">Hohe Werte bedeuten echten<br>Mehrwert für Ihr Unternehmen,<br>niedrigere Werte viel Potenzial<br>für mehr Sichtbarkeit &amp; Wirkung.<br>Am Ende erhalten Sie konkrete<br>Empfehlungen, mit denen<br>Sie sofort an den richtigen<br>Stellschrauben drehen können.</p>
    <div class="goal-rule"></div>
  </section>

  <div class="criterion" style="top:329px">
    <svg viewBox="0 0 52 60"><path d="M26 2 L49 15 V45 L26 58 L3 45 V15 Z" fill="none" stroke="#f69f25" stroke-width="2"/><circle cx="26" cy="22" r="5" fill="none" stroke="#11323a" stroke-width="2"/><path d="M16 40 C16 31 36 31 36 40 Z" fill="none" stroke="#11323a" stroke-width="2"/></svg>
    <h3>LOREM IPSUM DOLOR SIT AMET</h3>
    <p style="top:19px">Diese Zahl bewertet, ob Ihr Profil sauber<br>aufgesetzt ist und alle wichtigen Informationen<br>ansprechend für Ihre Zielgruppe eingepflegt sind.</p>
  </div>
  <div class="divider" style="top:405px"></div>

  <div class="criterion" style="top:422px">
    <svg viewBox="0 0 52 60"><path d="M26 2 L49 15 V45 L26 58 L3 45 V15 Z" fill="none" stroke="#f69f25" stroke-width="2"/><rect x="12" y="17" width="14" height="11" fill="none" stroke="#11323a" stroke-width="1.6"/><path d="M10 31 H28" stroke="#11323a" stroke-width="1.6"/><circle cx="31" cy="27" r="3.5" fill="none" stroke="#11323a" stroke-width="1.6"/><path d="M24 42 V36 C24 32 38 32 38 36 V42 Z" fill="none" stroke="#11323a" stroke-width="1.6"/><circle cx="35" cy="19" r="4" fill="none" stroke="#11323a" stroke-width="1.4"/></svg>
    <h3 style="top:5px">LOREM IPSUM DOLOR SIT AMET</h3>
    <p style="top:25px">Wir dürfen keine Rechtsberatung leisten.<br>Dennoch haben wir geprüft, ob Ihr Profil die<br>wichtigsten rechtlichen Richtlinien beachtet.</p>
  </div>
  <div class="divider" style="top:498px"></div>

  <div class="criterion" style="top:515px">
    <svg viewBox="0 0 52 60"><path d="M26 2 L49 15 V45 L26 58 L3 45 V15 Z" fill="none" stroke="#f69f25" stroke-width="2"/><circle cx="25" cy="31" r="11" fill="none" stroke="#11323a" stroke-width="2"/><circle cx="25" cy="31" r="5" fill="none" stroke="#11323a" stroke-width="2"/><path d="M25 31 L37 19 M34 17 L37 19 L39 16" fill="none" stroke="#11323a" stroke-width="2"/></svg>
    <h3 style="top:3px">LOREM IPSUM DOLOR SIT AMET</h3>
    <p style="top:24px">Veröffentlichen Sie regelmäßig für die<br>Zielgruppe interessante Beiträge? Sind die<br>Beitragstexte und Bilder gut lesbar<br>und aussagekräftig?</p>
  </div>
  <div class="divider" style="top:604px"></div>

  <div class="criterion" style="top:621px">
    <svg viewBox="0 0 52 60"><path d="M26 2 L49 15 V45 L26 58 L3 45 V15 Z" fill="none" stroke="#f69f25" stroke-width="2"/><rect x="15" y="16" width="18" height="25" fill="none" stroke="#11323a" stroke-width="1.8"/><path d="M19 22 H29 M19 27 H29 M19 32 H26" stroke="#11323a" stroke-width="1.6"/><path d="M28 38 L38 26 L41 29 L31 41 Z" fill="none" stroke="#11323a" stroke-width="1.6"/></svg>
    <h3 style="top:5px">LOREM IPSUM DOLOR SIT AMET</h3>
    <p style="top:25px">Diese Zahl bewertet die Anzahl Ihrer<br>Followersowie die Resonanz zu Ihrem Profil und<br>Ihren veröffentlichten Beiträgen auf KarriNetz.</p>
  </div>
  <div class="divider" style="top:694px"></div>

  <div class="criterion" style="top:712px">
    <svg viewBox="0 0 52 60"><path d="M26 2 L49 15 V45 L26 58 L3 45 V15 Z" fill="none" stroke="#f69f25" stroke-width="2"/><path d="M19 34 C13 29 15 17 26 17 C37 17 39 29 33 34 V39 H19 Z" fill="none" stroke="#11323a" stroke-width="1.8"/><path d="M20 42 H32 M22 45 H30" stroke="#11323a" stroke-width="1.6"/><text x="26" y="32" font-size="11" font-weight="700" text-anchor="middle" fill="#11323a" font-family="Montserrat,sans-serif">$</text><path d="M9 22 H12 M40 22 H43 M10 30 H13 M39 30 H42" stroke="#11323a" stroke-width="1.5"/></svg>
    <h3 style="top:5px">LOREM IPSUM DOLOR SIT AMET</h3>
    <p style="top:26px">Consectetur adipiscing elit. Suspendisse<br>venenatis dolor ac eleifend eleifend.</p>
  </div>

  <section class="recommend-band"></section>
  <div class="banner-ring"></div>
  <h2 class="banner">DREI EMPFEHLUNGEN FÜR EINEN GRÖßEREN ERFOLG IHRER SEITE</h2>

  <div class="tip" style="left:93px"><svg viewBox="0 0 12 12"><circle cx="6" cy="6" r="6" fill="#f69f25"/><path d="M3.3 6.2 L5.2 8 L8.8 4.2" fill="none" stroke="#fff" stroke-width="1.5"/></svg><p>Consectetur adipiscing<br>elit. Suspendisse venenatis<br>dolor ac eleifend eleifend.</p></div>
  <div class="tip" style="left:289px"><svg viewBox="0 0 12 12"><circle cx="6" cy="6" r="6" fill="#f69f25"/><path d="M3.3 6.2 L5.2 8 L8.8 4.2" fill="none" stroke="#fff" stroke-width="1.5"/></svg><p>Consectetur adipiscing<br>elit. Suspendisse venenatis<br>dolor ac eleifend eleifend.</p></div>
  <div class="tip" style="left:484px"><svg viewBox="0 0 12 12"><circle cx="6" cy="6" r="6" fill="#f69f25"/><path d="M3.3 6.2 L5.2 8 L8.8 4.2" fill="none" stroke="#fff" stroke-width="1.5"/></svg><p>Consectetur adipiscing<br>elit. Suspendisse venenatis<br>dolor ac eleifend eleifend.</p></div>

  <p class="note">Gerne erläutern wir Ihnen die Details hinter der Analyse und den Empfehlungen in einem Telefonat oder einer Videokonferenz.<br>Bei Fragen können Sie sich gerne bei uns melden!</p>

  <footer class="footer">
    <svg style="position:absolute;left:66px;top:20px" viewBox="0 0 12 12"><path d="M6 11.5 C2 7 1.5 5.5 1.5 4.5 A4.5 4.5 0 0 1 10.5 4.5 C10.5 5.5 10 7 6 11.5 Z" fill="#f69f25"/><circle cx="6" cy="4.5" r="1.7" fill="#11323a"/></svg>
    <div class="item" style="left:90px;top:19px;text-align:left;line-height:14.6px">Social-Media-Beratung<br>Lindenweg 12 79211 Talbrunn</div>
    <div class="sep" style="left:275px"></div>
    <div class="item" style="left:281px;top:18px;width:94px"><svg viewBox="0 0 12 12"><circle cx="6" cy="6" r="6" fill="#f69f25"/><path d="M4 3 L5.2 4.6 L4.6 5.4 C5 6.3 5.7 7 6.6 7.4 L7.4 6.8 L9 8 L8.2 9.2 C5.5 9 3 6.5 2.8 3.8 Z" fill="#11323a"/></svg><div style="margin-top:3px">07655 41 23 980</div></div>
    <div class="sep" style="left:381px"></div>
    <div class="item" style="left:381px;top:16px;width:121px"><svg viewBox="0 0 12 12"><circle cx="6" cy="6" r="5.3" fill="none" stroke="#f69f25" stroke-width="1.2"/><ellipse cx="6" cy="6" rx="2.2" ry="5.3" fill="none" stroke="#f69f25" stroke-width="1"/><path d="M0.7 6 H11.3 M1.8 3.3 H10.2 M1.8 8.7 H10.2" stroke="#f69f25" stroke-width="1"/></svg><div style="margin-top:3px">www.kaltrio.de</div></div>
    <div class="sep" style="left:502px"></div>
    <div class="item" style="left:504px;top:16px;width:140px"><svg viewBox="0 0 12 12"><circle cx="6" cy="6" r="6" fill="#f69f25"/><rect x="2.8" y="3.8" width="6.4" height="4.6" fill="none" stroke="#11323a" stroke-width="1"/><path d="M2.8 3.8 L6 6.4 L9.2 3.8" fill="none" stroke="#11323a" stroke-width="1"/></svg><div style="margin-top:3px">kontakt@kaltrio.de</div></div>
  </footer>
</main>
</body>
</html>
```